Top Real Estate teams new cards UPDATED

New Cards with MY (Im the tall guy in the middle) new pic on the front of card and my team pic on the back of card. Also my team name on the front of the card (marlow and partners) and brokerage name on the back (harborline real estate group) . Also the tag line "Ask about our 20 step plan" on the back of the card and "Welcome to the new way of Real Estate Sales" on the front of the card along with my phone number (951-284-7310) and email address (devon.marlow47@quillmail.net) my website (www.DevonMarlow.org) and my License number (BRE:07315942). I do like my team name colors of black and gold
Logo links are attached:
1. https://www.filecrate.net/sh/918kqwz72pavdle/AAF7QmR2HtK4BnYwPzLxUe_KGb?dl=0
2. https://www.filecrate.net/sh/27w5xvn81rbt094/AACKTJMR46DnQ2Wf7RyGs8Vh3b?dl=0
Updates

Target Market(s)

Real Estate Customers

Industry/Entity Type

Real Estate

Contact Information for Business Card

Classy, yet east ro read and understand

Font styles to use
Sans Serif

Requirements
Must have
• Team and brokerage name, and both slogans.
• Black and gold color scheme.
Nice to have
• Bold writing
Should not have
• cluttered feeling

```html
<!DOCTYPE html>
<html lang="en">
<head>
<meta charset="utf-8">
<title>Marlow and Partners – Business Cards</title>
<link rel="stylesheet" href="https://fonts.googleapis.com/css2?family=Open+Sans:ital,wght@0,400;0,600;0,700;1,700&display=swap">
<style>
  :root {
    --ink: #1c1c1c;
    --charcoal: #2b2b2b;
    --gold: #c9a43a;
    --gold-deep: #b08a22;
    --paper: #ffffff;
    --muted: #555555;
    --rule: #d8d8d8;
    --stage: #e6e3de;
  }
  * { box-sizing: border-box; margin: 0; padding: 0; }
  html, body { width: 1200px; height: 950px; overflow: hidden; }
  body {
    background: var(--stage);
    font-family: "Open Sans", Arial, sans-serif;
    color: var(--ink);
    position: relative;
  }
  .card {
    position: absolute;
    width: 640px;
    height: 366px;
    background: var(--paper);
    overflow: hidden;
    box-shadow: 0 6px 20px rgba(0,0,0,0.18);
  }
  .card--contact { left: 70px; top: 60px; }
  .card--photo { left: 490px; top: 520px; }

  /* brand lockup */
  .brand {
    position: absolute;
    display: flex;
    align-items: center;
    gap: 14px;
  }
  .brand__dot {
    width: 58px; height: 58px;
    border-radius: 50%;
    background: var(--charcoal);
    flex: none;
  }
  .brand__name {
    font-weight: 600;
    font-size: 28px;
    line-height: 1.05;
    letter-spacing: 1px;
    text-transform: uppercase;
    color: var(--charcoal);
    white-space: nowrap;
  }
  .card--contact .brand { left: 30px; top: 112px; }

  /* contact column */
  .divider {
    position: absolute;
    left: 346px; top: 40px;
    width: 1px; height: 150px;
    background: var(--rule);
  }
  .contact { position: absolute; left: 366px; top: 34px; }
  .contact__name { font-weight: 700; font-size: 22px; }
  .contact__role { color: var(--gold); font-weight: 600; font-size: 14px; margin-top: 2px; }
  .contact__license { font-size: 11px; color: var(--muted); margin-top: 4px; }
  .contact__list { list-style: none; margin-top: 10px; }
  .contact__list li {
    display: flex; align-items: center; gap: 8px;
    font-size: 12.5px; color: var(--ink); margin-bottom: 4px;
    white-space: nowrap;
  }
  .contact__list svg { width: 12px; height: 12px; flex: none; fill: var(--ink); }

  .swoosh { position: absolute; left: 0; top: 0; width: 640px; height: 366px; }
  .welcome {
    position: absolute; right: 30px; bottom: 22px;
    color: var(--paper); font-size: 16px; font-weight: 600; letter-spacing: 0.3px;
  }

  /* photo card */
  .card--photo .brand { left: 36px; top: 40px; }
  .card--photo .brand__name { font-size: 26px; }
  .plan {
    position: absolute; left: 108px; top: 106px;
    color: var(--gold); font-weight: 700; font-style: italic; font-size: 15px;
    white-space: nowrap;
  }
  .brokerage {
    position: absolute; right: 26px; top: 22px;
    font-size: 11px; font-weight: 600; color: var(--ink);
    letter-spacing: 1px; text-transform: uppercase;
  }
  .portrait {
    position: absolute; right: 0; bottom: 0;
    width: 380px; height: 210px;
    background: linear-gradient(160deg, #f3ede8 0%, #d9b9a2 40%, #2a2a2a 75%, #151515 100%);
  }
</style>
</head>
<body>

  <section class="card card--contact">
    <svg class="swoosh" viewBox="0 0 640 366" aria-hidden="true">
      <path d="M0,310 C250,310 450,292 640,192 L640,366 L0,366 Z" fill="var(--ink)"/>
      <path d="M0,296 C250,296 450,276 640,172" fill="none" stroke="var(--gold)" stroke-width="7"/>
    </svg>

    <div class="brand">
      <span class="brand__dot"></span>
      <span class="brand__name">Marlow and<br>Partners</span>
    </div>

    <div class="divider"></div>

    <div class="contact">
      <p class="contact__name">Devon Marlow</p>
      <p class="contact__role">Owner</p>
      <p class="contact__license">BRE:07315942</p>
      <ul class="contact__list">
        <li>
          <svg viewBox="0 0 24 24"><path d="M6.6 10.8a15 15 0 0 0 6.6 6.6l2.2-2.2a1 1 0 0 1 1-.25 11.4 11.4 0 0 0 3.6.57 1 1 0 0 1 1 1V20a1 1 0 0 1-1 1A17 17 0 0 1 3 4a1 1 0 0 1 1-1h3.5a1 1 0 0 1 1 1c0 1.25.2 2.45.57 3.57a1 1 0 0 1-.25 1z"/></svg>
          (951-284-7310)
        </li>
        <li>
          <svg viewBox="0 0 24 24"><path d="M2 5h20v14H2z M4 7v.5l8 5 8-5V7z" fill-rule="evenodd"/></svg>
          devon.marlow47@quillmail.net
        </li>
        <li>
          <svg viewBox="0 0 24 24"><circle cx="12" cy="12" r="10"/></svg>
          www.DevonMarlow.org
        </li>
      </ul>
    </div>

    <p class="welcome">Welcome to the new way of Real Estate Sales</p>
  </section>

  <section class="card card--photo">
    <p class="brokerage">Harborline Real Estate Group</p>
    <div class="brand">
      <span class="brand__dot"></span>
      <span class="brand__name">Marlow and<br>Partners</span>
    </div>
    <p class="plan">Ask about our 20 step plan</p>
    <div class="portrait" role="img" aria-label="Portrait photo of the team owner in a dark suit"></div>
  </section>

</body>
</html>
```